Law Firm Stationery/Cards
Penhallow & Birchmont
Law Firm Stationery/Cards -
Creative Brief
Use specific fonts
Use whatever fonts look best
Professional
Martin K. Birchmont
Attorney at Law
7150 E. Marlow Avenue Suite 230 Tampa, FL 33614
mbirchmont@penhallowbirchmont.com
www.penhallowbirchmont.com
Include in business card: Social Security Disability Board Certified in Workers' Compensation Stationery/Letterhead should include Attorney names: Daniel T. Penhallow* Martin K. Birchmont* * Board Certified in Workers' Compensation Attorney include the practice areas "Social Security Disability" and "Workers' Compensation" on the letterhead We'd like it to be flexible for adding additional office locations or additional attorneys in the future. I'll upload our current letterhead for informational purposes only - not design.
Designer's choice

```html
<!DOCTYPE html>
<html lang="en">
<head>
<meta charset="utf-8">
<title>Penhallow &amp; Birchmont — Stationery</title>
<link rel="stylesheet" href="https://fonts.googleapis.com/css2?family=Cinzel:wght@500&family=EB+Garamond:ital,wght@0,400;0,500;1,400&display=swap">
<style>
  :root {
    --backdrop: #8e8f91;
    --paper: #ffffff;
    --paper-edge: #e4e4e4;
    --gold: #c48f34;
    --gold-light: #d9a64a;
    --bronze: #8a6222;
    --brown: #5e4217;
    --brown-dark: #4a3210;
    --ink: #5a5a5a;
    --shadow: rgba(0,0,0,.35);
  }
  * { box-sizing: border-box; margin: 0; padding: 0; }
  html, body { width: 1200px; height: 785px; overflow: hidden; }
  body { background: var(--backdrop); font-family: "EB Garamond", Georgia, serif; color: var(--ink); }
  .board { position: relative; width: 1200px; height: 785px; }

  .sheet { position: absolute; background: var(--paper); box-shadow: 0 4px 14px var(--shadow); overflow: hidden; }

  .mark { display: inline-block; background: var(--gold); flex: none; }
  .brand { display: flex; align-items: center; gap: 10px; }
  .brand-name { font-family: "Cinzel", "Times New Roman", serif; font-weight: 500; color: var(--gold); letter-spacing: .04em; white-space: nowrap; }
  .brand-sub { font-size: 7px; letter-spacing: .2em; color: var(--gold); text-transform: uppercase; margin-top: 2px; }

  /* envelope backs */
  .envelope-back { left: 28px; width: 464px; height: 176px; }
  .envelope-back svg { position: absolute; inset: 0; }
  .envelope-back .flap-mark { position: absolute; left: 219px; width: 26px; height: 26px; background: var(--paper); opacity: .9; }
  .env-1 { top: 26px; }
  .env-2 { top: 116px; }
  .env-3 { top: 206px; }

  /* envelope front */
  .envelope-front { left: 118px; top: 350px; width: 512px; height: 192px; }
  .envelope-front .brand { position: absolute; left: 18px; top: 24px; }
  .envelope-front .brand-name { font-size: 14px; }
  .envelope-front .mark { width: 24px; height: 24px; }
  .envelope-front .return-address { position: absolute; left: 52px; top: 82px; font-size: 8px; line-height: 1.35; color: var(--ink); }
  .envelope-front .corner-mark { position: absolute; right: 22px; bottom: 20px; width: 24px; height: 24px; background: var(--gold); }
  .envelope-front .base-band { position: absolute; left: 0; right: 0; bottom: 8px; height: 3px; background: var(--brown); }

  /* letterhead */
  .letterhead { left: 504px; top: 22px; width: 446px; height: 634px; }
  .letterhead .brand { position: absolute; left: 30px; top: 32px; }
  .letterhead .brand-name { font-size: 17px; }
  .letterhead .mark { width: 30px; height: 30px; }
  .letterhead .seal { position: absolute; right: 34px; top: 28px; width: 46px; height: 46px; border: 2px solid #9a9a9a; border-radius: 4px; }
  .attorneys { position: absolute; left: 52px; top: 92px; font-style: italic; font-size: 12.5px; line-height: 1.3; color: var(--bronze); font-weight: 500; }
  .attorneys .note { font-style: normal; font-size: 7px; color: var(--ink); margin-top: 8px; font-weight: 400; }
  .practice { font-style: normal; font-size: 7px; color: var(--ink); font-weight: 400; line-height: 1.35; }
  .letterhead .rule { position: absolute; left: 30px; right: 30px; bottom: 84px; height: 1px; background: var(--gold); }
  .letterhead .footer { position: absolute; left: 52px; bottom: 44px; font-size: 7.5px; line-height: 1.4; }
  .letterhead .footer .web { color: var(--bronze); }
  .letterhead .corner-mark { position: absolute; right: 30px; bottom: 28px; width: 30px; height: 30px; background: var(--gold); }

  /* business cards */
  .card { position: absolute; left: 989px; width: 194px; height: 100px; box-shadow: 0 3px 10px var(--shadow); overflow: hidden; }
  .card.is-brown { background: linear-gradient(135deg, var(--bronze), var(--brown-dark)); }
  .card.is-gold { background: linear-gradient(135deg, var(--gold-light), var(--bronze)); }
  .card.is-white { background: var(--paper); }
  .card .mark { position: absolute; left: 18px; top: 41px; width: 18px; height: 18px; background: rgba(255,255,255,.85); }
  .card .tagline { position: absolute; left: 50px; top: 36px; font-size: 7.5px; line-height: 1.35; color: #f3e6cc; }

  .card-front .brand { position: absolute; left: 10px; top: 36px; gap: 6px; }
  .card-front .brand-name { font-size: 8px; letter-spacing: .02em; }
  .card-front .mark { position: static; width: 14px; height: 14px; background: var(--gold); }
  .card-front .contact { position: absolute; left: 98px; top: 24px; font-size: 5px; line-height: 1.4; white-space: nowrap; }
  .card-front .contact .name { font-size: 8.5px; color: var(--bronze); font-weight: 500; }
  .card-front .base-band { position: absolute; left: 0; right: 0; bottom: 6px; height: 3px; background: var(--brown); }

  .card-logo { left: 1000px; top: 14px; width: 184px; height: 90px; }
  .card-logo .brand { position: absolute; left: 12px; top: 34px; gap: 7px; }
  .card-logo .brand-name { font-size: 9px; letter-spacing: .02em; }
  .card-logo .mark { position: static; width: 20px; height: 20px; background: var(--gold); }
</style>
</head>
<body>
<main class="board">

  <div class="sheet envelope-back env-1">
    <svg width="464" height="176" viewBox="0 0 464 176"><polygon points="0,0 464,0 232,150" fill="#f2f2f2" stroke="var(--paper-edge)"/></svg>
  </div>
  <div class="sheet envelope-back env-2">
    <svg width="464" height="176" viewBox="0 0 464 176"><defs><linearGradient id="flapBrown" x1="0" y1="0" x2="0" y2="1"><stop offset="0" stop-color="#7a5620"/><stop offset="1" stop-color="#a27230"/></linearGradient></defs><polygon points="0,0 464,0 232,150" fill="url(#flapBrown)"/></svg>
    <span class="flap-mark" style="top:112px"></span>
  </div>
  <div class="sheet envelope-back env-3">
    <svg width="464" height="176" viewBox="0 0 464 176"><defs><linearGradient id="flapGold" x1="0" y1="0" x2="0" y2="1"><stop offset="0" stop-color="#c68c2c"/><stop offset="1" stop-color="#e0a449"/></linearGradient></defs><polygon points="0,0 464,0 232,150" fill="url(#flapGold)"/></svg>
    <span class="flap-mark" style="top:112px"></span>
  </div>

  <section class="sheet letterhead">
    <div class="brand">
      <span class="mark"></span>
      <div>
        <div class="brand-name">Penhallow &amp; Birchmont</div>
        <div class="brand-sub">Attorneys at Law</div>
      </div>
    </div>
    <span class="seal" role="img" aria-label="Certification badge"></span>
    <div class="attorneys">
      <div>Daniel T. Penhallow*</div>
      <div>Martin K. Birchmont*</div>
      <div class="note">* Board Certified Workers' Compensation Attorney</div>
      <div class="practice">Social Security Disability<br>Workers' Compensation</div>
    </div>
    <div class="rule"></div>
    <div class="footer">
      7150 E. Marlow Avenue Suite 230 Tampa, FL 33614<br>
      Phone 813.555.0142 &nbsp; Fax 813.555.0143<br>
      <span class="web">www.penhallowbirchmont.com</span>
    </div>
    <span class="corner-mark"></span>
  </section>

  <section class="sheet envelope-front">
    <div class="brand">
      <span class="mark"></span>
      <div>
        <div class="brand-name">Penhallow &amp; Birchmont</div>
        <div class="brand-sub">Attorneys at Law</div>
      </div>
    </div>
    <div class="return-address">7150 E. Marlow Avenue<br>Suite 230<br>Tampa, FL 33614</div>
    <div class="base-band"></div>
    <span class="corner-mark"></span>
  </section>

  <section class="sheet card-logo">
    <div class="brand">
      <span class="mark"></span>
      <span class="brand-name">Penhallow &amp; Birchmont</span>
    </div>
  </section>

  <div class="card is-brown" style="top:188px;">
    <span class="mark"></span>
    <div class="tagline">Social Security Disability<br>Board Certified Workers'<br>Compensation</div>
  </div>
  <div class="card is-gold" style="top:308px;">
    <span class="mark"></span>
    <div class="tagline">Social Security Disability<br>Board Certified Workers'<br>Compensation</div>
  </div>
  <div class="card is-brown" style="top:428px;">
    <span class="mark"></span>
    <div class="tagline">Social Security Disability<br>Board Certified Workers'<br>Compensation</div>
  </div>
  <div class="card is-white card-front" style="top:548px;">
    <div class="brand">
      <span class="mark"></span>
      <span class="brand-name">Penhallow &amp;<br>Birchmont</span>
    </div>
    <div class="contact">
      <div class="name">Martin K. Birchmont</div>
      Attorney at Law<br>
      7150 E. Marlow Avenue Suite 230<br>
      Tampa, FL 33614<br>
      Phone 813.555.0142<br>
      mbirchmont@penhallowbirchmont.com<br>
      www.penhallowbirchmont.com
    </div>
    <div class="base-band"></div>
  </div>

</main>
</body>
</html>
```